Lark Stewardship Business Card design

We need a creative business card design for our hospitality management company
We need the following information:
Our business Logo: Lark Stewardship
Name: Mira Dalvorsen
Phone number: 0468 319 542
Email: mira@larkstewardship.com.au
Address: 214/53 Pemberly Street, Kestrel Bay 3291
Web: www.larkstewardship.com.au
I need the design to be a working file so that I can insert the names and numbers of the other staff members of our business.
The cards need to be 90 x 40mm
Thanks
Hospitality

```html
<!DOCTYPE html>
<html lang="en">
<head>
<meta charset="utf-8">
<title>Lark Stewardship Business Card</title>
<link rel="stylesheet" href="https://fonts.googleapis.com/css2?family=Arimo:wght@400;700&display=swap">
<style>
  :root {
    --backdrop: #1b1b1d;
    --card: #f7f7f6;
    --navy: #1f4a78;
    --navy-deep: #173a60;
    --sky: #4a9fd8;
    --ink: #3e3f42;
    --white: #ffffff;
  }
  * { box-sizing: border-box; margin: 0; padding: 0; }
  html, body {
    width: 1200px;
    height: 805px;
    overflow: hidden;
    background: var(--backdrop);
    font-family: "Arimo", Arial, sans-serif;
  }
  .canvas {
    position: relative;
    width: 1200px;
    height: 805px;
  }
  .card {
    position: absolute;
    left: 240px;
    width: 720px;
    height: 320px;
    border-radius: 36px;
    background: var(--card);
    overflow: hidden;
  }
  .card--front { top: 50px; }
  .card--back { top: 435px; }
  .card-art {
    position: absolute;
    inset: 0;
    width: 720px;
    height: 320px;
  }

  /* Wordmark: square above name */
  .brand {
    position: absolute;
    display: flex;
    flex-direction: column;
    align-items: center;
  }
  .brand-mark { background: var(--navy); }
  .brand-name {
    font-weight: 700;
    color: var(--navy);
    text-transform: uppercase;
    letter-spacing: 0.5px;
    white-space: nowrap;
    line-height: 1;
  }
  .card--front .brand {
    left: 0;
    right: 0;
    top: 62px;
    gap: 14px;
  }
  .card--front .brand-mark { width: 78px; height: 78px; }
  .card--front .brand-name { font-size: 36px; }
  .card--back .brand {
    right: 34px;
    top: 22px;
    gap: 8px;
  }
  .card--back .brand-mark { width: 44px; height: 44px; }
  .card--back .brand-name { font-size: 19px; }

  /* Back details */
  .holder-name {
    position: absolute;
    left: 30px;
    top: 155px;
    font-size: 26px;
    line-height: 34px;
    font-weight: 700;
    color: var(--white);
  }
  .website {
    position: absolute;
    right: 30px;
    top: 116px;
    font-size: 16px;
    line-height: 20px;
    color: var(--white);
  }
  .contact {
    position: absolute;
    left: 30px;
    top: 200px;
    font-size: 17px;
    line-height: 23px;
    color: var(--ink);
    font-style: normal;
  }
</style>
</head>
<body>
<main class="canvas">

  <section class="card card--front" aria-label="Card front">
    <svg class="card-art" viewBox="0 0 720 320" aria-hidden="true">
      <rect class="stripe stripe--navy" x="0" y="232" width="720" height="14" fill="var(--navy)"/>
      <rect class="stripe stripe--sky" x="0" y="250" width="720" height="12" fill="var(--sky)"/>
      <rect class="stripe stripe--navy-thin" x="0" y="266" width="720" height="7" fill="var(--navy-deep)"/>
    </svg>
    <div class="brand">
      <span class="brand-mark"></span>
      <span class="brand-name">Lark Stewardship</span>
    </div>
  </section>

  <section class="card card--back" aria-label="Card back">
    <svg class="card-art" viewBox="0 0 720 320" aria-hidden="true">
      <polygon class="band" fill="var(--navy)"
        points="0,152 240,152 284,108 720,108 720,144 296,144 252,188 0,188"/>
      <rect class="band-accent" x="318" y="108" width="8" height="36" fill="var(--sky)"/>
    </svg>
    <div class="brand">
      <span class="brand-mark"></span>
      <span class="brand-name">Lark Stewardship</span>
    </div>
    <p class="website">www.larkstewardship.com.au</p>
    <h1 class="holder-name">Mira Dalvorsen</h1>
    <address class="contact">
      0468 319 542<br>
      mira@larkstewardship.com.au<br>
      214/53 Pemberly Street,<br>
      Kestrel Bay 3291
    </address>
  </section>

</main>
</body>
</html>
```